I want our new logo design to guide the colors and look of the home page. I want it to be vibrant and contemporary. We are a new religious education publishing company. I would like any colors used to describe the product below to be bright and cheerful, but also to look good with our logo colors
On our home page we are introducing a new product for second graders. The product name should look child friendly, but not silly. If there is a way to add reverence to the words FIRST RECONCILIATION and FIRST EUCHARIST, and still make it look like it is a product for children, that would be great.
The product will be called:
Wayfinder Gathering Set for the Welcoming Room
FIRST RECONCILIATION
FIRST EUCHARIST
THE PRODUCT DESCRIPTION SHOULD BE AS FOLLOWS
Field tested and designed for the special needs inclusive classroom
Kit includes high impact visuals, hands-on activities, manipulatives, games, and other teaching aids for total engagement of ALL students
Detailed catechist lesson plans to maximize learning and retention
Cost effective reusable kit
Bilingual
Somewhere it should say COMING SOON, because the product is not ready yet, but we are promoting it. I don't have a picture of this product yet, but above the product description, we need an empty box that we'll use when we're ready to upload the picture of the kit.
There should also be a statement near the product description that says: To learn more about the Wayfinder Set for the Welcoming Room, click here.
Web page links:
About Us
Products
Resources
Contact Us
I would also like a few links to be featured on the home page:
Lanterns Along the Young Road....learn more
"What Calls Us Home?"....learn more
Could It Be Something Else Entirely?...learn more
The Map and the Path...learn more
Open Table Storytelling
I have increased my budget and clarified my brief so that it's easier to understand. It's basically just a home page and a template for the other pages. There is no content on the other web pages that you have to work on. I just need a well designed home page and a nice template for the other pages.
Reason: I am extending the deadline for 2 days so that templates can be designed for 5 additional web pages. Please make each template a little different from the way you designed the home page. These pages can have blank picture boxes and dummy text to save you time. I am only interested in layout for the addtional pages. Thank you!
We've made a selection and wanted to thank all of you for your wonderful designs!

```html
<!DOCTYPE html>
<html lang="en">
<head>
<meta charset="utf-8">
<title>About Us – Lantern Road Catechetics</title>
<link href="https://fonts.googleapis.com/css2?family=Arimo:ital,wght@0,400;0,700;1,400&display=swap" rel="stylesheet">
<style>
:root{
  --brand-red:#c4161c;
  --brand-orange:#f39a00;
  --bg-deep:#a30f19;
  --ink:#222;
  --ink-soft:#333;
  --muted:#777;
  --rule:#e8e8e8;
  --panel:#fff;
}
*{margin:0;padding:0;box-sizing:border-box}
html,body{width:1200px;height:992px;overflow:hidden}
body{
  font-family:"Arimo",Arial,sans-serif;
  color:var(--ink-soft);
  background:
    radial-gradient(ellipse 620px 260px at 600px 40px,rgba(240,120,30,.85),rgba(240,120,30,0) 100%),
    radial-gradient(ellipse 900px 700px at 600px 300px,#d5361f,var(--bg-deep) 80%);
  position:relative;
}
.topbar{position:absolute;top:8px;right:96px;display:flex;align-items:center;gap:6px;color:#fff;font-size:13px}
.topbar .phone{display:flex;align-items:center;gap:6px;margin-right:16px}
.social{display:flex;gap:4px}
.social span{width:16px;height:16px;border-radius:2px}
.social span:nth-child(1){background:#3b5ea0}
.social span:nth-child(2){background:#3fb3e5}
.social span:nth-child(3){background:#2a73b4}
.social span:nth-child(4){background:#f08a1c}

.panel{position:absolute;left:77px;top:38px;width:1035px;height:828px;background:var(--panel);border-radius:8px;overflow:hidden}
.header{height:114px;background:linear-gradient(#fff,#f1f1f1);border-bottom:3px solid var(--brand-red);position:relative;box-shadow:0 4px 8px rgba(0,0,0,.08)}
.brand{position:absolute;left:40px;top:42px}
.brand .name{font-size:25px;font-weight:700;color:var(--brand-red);line-height:1;white-space:nowrap}
.nav{position:absolute;top:43px;left:440px;display:flex;font-size:15px}
.nav a{color:var(--ink-soft);text-decoration:none;display:block;height:29px;line-height:29px;text-align:center}
.nav a:nth-child(1){width:90px}
.nav a:nth-child(2){width:90px;margin-left:34px}
.nav a:nth-child(3){width:90px;margin-left:4px}
.nav a:nth-child(4){width:110px;margin-left:10px}
.nav a:nth-child(5){width:110px;margin-left:4px}
.nav a.active{background:linear-gradient(#f79a25,#d4341b);color:#fff;border-radius:6px}

.main{position:absolute;left:29px;top:158px;width:650px}
h1{font-size:19px;font-weight:400;color:#111;line-height:24px;padding-bottom:14px;border-bottom:1px solid var(--rule)}
h1 .line{display:block}
.hl{color:var(--brand-red)}
.main p{font-size:12.5px;line-height:19px;margin-top:17px}
.main p + p{margin-top:19px}
.main em{color:var(--muted)}
.bullets{list-style:none;margin-top:19px;font-size:12.5px;line-height:19px}
.bullets li{padding-left:17px;position:relative}
.bullets li::before{content:"";position:absolute;left:0;top:6px;border-left:6px solid var(--brand-red);border-top:4px solid transparent;border-bottom:4px solid transparent}
.bullets li.hl{color:var(--brand-red)}
h2{font-size:15.5px;font-weight:400;color:#111;margin-top:38px}
.main h2 + p{margin-top:13px}
.gallery{display:flex;gap:30px;margin-top:32px}
.photo{width:197px;height:126px;border-radius:6px;position:relative;display:flex;align-items:center;justify-content:center}
.photo.students{background:linear-gradient(135deg,#e9dfd6,#c88a5a 55%,#3a3a3a)}
.photo.outdoor{background:linear-gradient(135deg,#6f7a55,#3b3a32 60%,#222)}
.photo.classroom{background:linear-gradient(135deg,#cfd9e6,#9fb3c8 50%,#6a7a86)}

.aside{position:absolute;left:709px;top:158px;width:302px}
.aside h3{font-size:19px;font-weight:400;color:#111;margin-top:9px}
.aside .item{font-size:12.5px;line-height:15px;margin-top:13px}
.aside .label{color:var(--brand-red);display:block}
.aside .block{border-bottom:1px solid var(--rule);width:290px}
.aside .about{padding-bottom:31px}
.aside .about .item + .item{margin-top:31px}
.aside .staff{margin-top:28px;padding-bottom:30px}
.aside .staff .item + .item{margin-top:12px}

.footer{position:absolute;top:881px;left:0;width:1200px;text-align:center;color:#fff;font-size:12.5px}
.footer .accent{color:var(--brand-orange)}
</style>
</head>
<body>
<div class="topbar">
  <div class="phone">
    <svg width="18" height="12" viewBox="0 0 18 12" aria-hidden="true"><path d="M1 5 C1 1 17 1 17 5 L14 6 L13 4 L5 4 L4 6 Z" fill="#fff"/><rect x="4" y="6" width="10" height="5" rx="1" fill="#fff"/></svg>
    <span>555-0142-7730</span>
  </div>
  <div class="social" aria-label="Social links"><span></span><span></span><span></span><span></span></div>
</div>

<div class="panel">
  <header class="header">
    <div class="brand"><span class="name">Lantern Road Catechetics</span></div>
    <nav class="nav">
      <a href="#">Home</a>
      <a href="#" class="active">About Us</a>
      <a href="#">Products</a>
      <a href="#">Resources</a>
      <a href="#">Contact Us</a>
    </nav>
  </header>

  <main class="main">
    <h1><span class="line">Lorem ipsum dolor sit amet, <span class="hl">consectetuer</span> adipiscing elit, sed diam</span><span class="line">nonummy nibh euismod tincidunt ut laoreet</span></h1>
    <p>Duis autem vel eum iriure dolor in hendrerit in vulputate velit esse molestie consequat, vel illum dolore eu feugiat nulla facilisis at vero eros et accumsan et iusto odio dignissim qui blandit praesent luptatum zzril delenit augue duis dolore te feugait nulla facilisi.</p>
    <p>Nam liber tempor cum soluta nobis eleifend option congue nihil imperdiet doming id quod mazim placerat facer possim assum. Typi non habent claritatem insitam; est usus legentis in iis qui facit eorum claritatem. Investigationes demonstraverunt lectores legere me lius quod ii legunt saepius. <em>Claritas est etiam processus</em> dynamicus, qui sequitur mutationem consuetudium lectorum. Mirum est notare quam littera gothica, quam nunc putamus parum claram, anteposuerit litterarum formas humanitatis per seacula quarta decima et quinta decima. Eodem modo typi, qui nunc nobis videntur parum clari, fiant sollemnes in futurum.</p>
    <ul class="bullets">
      <li>Ut wisi enim ad minim veniam, quis nostrud exerci tation ullamcorper.</li>
      <li class="hl">Duis autem vel eum iriure dolor in hendrerit in vulputate velit esse.</li>
      <li>Typi non habent claritatem insitam; est usus legentis in iis.</li>
    </ul>
    <h2>Claritas est etiam processus <span class="hl">dynamicus</span>, qui sequitur mutationem</h2>
    <p>Duis autem vel eum iriure dolor in hendrerit in vulputate velit esse molestie consequat, vel illum dolore eu feugiat nulla facilisis at vero eros et accumsan et iusto odio dignissim qui blandit praesent.</p>
    <div class="gallery">
      <div class="photo students" role="img" aria-label="Photo of smiling teenage students holding books"></div>
      <div class="photo outdoor" role="img" aria-label="Photo of students sitting together outdoors">
        <svg width="70" height="70" viewBox="0 0 70 70" aria-hidden="true"><circle cx="35" cy="35" r="30" fill="none" stroke="#fff" stroke-width="7"/><rect x="22" y="31" width="26" height="8" fill="#fff"/><rect x="31" y="22" width="8" height="26" fill="#fff"/></svg>
      </div>
      <div class="photo classroom" role="img" aria-label="Photo of students in a classroom raising hands"></div>
    </div>
  </main>

  <aside class="aside">
    <div class="block about">
      <h3>About Lantern Road Catechetics</h3>
      <div class="item"><span class="label">Vision</span>Ut wisi enim ad minim veniam, quis nostrud exerci tation ullamcorper suscipit lobortis nisl ut aliquip ex ea commodo consequat.</div>
      <div class="item"><span class="label">Mission</span>Nam liber tempor cum soluta nobis eleifend option congue nihil imperdiet doming id quod mazim placerat facer possim assum.</div>
    </div>
    <div class="block staff">
      <h3>Staff</h3>
      <div class="item"><span class="label">Anonymous</span>City here, Country</div>
      <div class="item"><span class="label">Anonymous</span>City here, Country</div>
      <div class="item"><span class="label">Anonymous</span>City here, Country</div>
    </div>
  </aside>
</div>

<footer class="footer">Copyright © 2011 Lantern Road <span class="accent">Catechetics</span>. All right reserved</footer>
</body>
</html>
```